Talbek vodka

With the logo attached in the subsequent file, a business card that reflects a premium and organic vodka. On the first side, the company logo in large. The names must be included on the back of the card (Mateo Ignacio Dalmau Ferrerons with the number +34 655 219 870 and Oriol Batlle Quintana and +34 677 341 592). The slogan "What binds us" and "Organic and permium vodka" in bold E-mail (talbekvodka@mailora.net); Website www.talbekvodkaorg.net

```html
<!DOCTYPE html>
<html lang="en">
<head>
<meta charset="utf-8">
<title>Talbek vodka – business card</title>
<link rel="stylesheet" href="https://fonts.googleapis.com/css2?family=Cinzel:wght@400;500&family=Open+Sans:wght@400;700&display=swap">
<style>
  :root {
    --backdrop: #3b3b3d;
    --card-grey: #838387;
    --card-white: #ffffff;
    --ink-light: #ffffff;
    --ink-grey: #8a8a8e;
    --ink-dark: #6f6f73;
    --rule: rgba(255,255,255,0.45);
  }
  * { margin: 0; padding: 0; box-sizing: border-box; }
  html, body { width: 1200px; height: 1200px; overflow: hidden; }
  body {
    background: var(--backdrop);
    position: relative;
    font-family: "Open Sans", Arial, sans-serif;
  }
  .card {
    position: absolute;
    left: 220px;
    width: 760px;
    height: 434px;
    box-shadow: 0 14px 30px rgba(0,0,0,0.35);
  }
  .card--front {
    top: 130px;
    background: var(--card-grey);
    border-radius: 70px 0 70px 0;
  }
  .card--back {
    top: 620px;
    background: var(--card-white);
    border-radius: 0 70px 0 70px;
  }

  /* front */
  .brand-name {
    font-family: "Cinzel", Georgia, serif;
    font-weight: 400;
    text-transform: uppercase;
    letter-spacing: 4px;
    white-space: nowrap;
  }
  .card--front .brand-name {
    position: absolute;
    top: 120px; left: 0; right: 0;
    text-align: center;
    font-size: 64px;
    color: var(--ink-light);
  }
  .slogan {
    position: absolute;
    top: 262px; left: 60px; right: 60px;
    text-align: center;
    font-family: "Cinzel", Georgia, serif;
    font-weight: 500;
    color: var(--ink-light);
    font-size: 21px;
    letter-spacing: 1.5px;
    line-height: 1.25;
  }
  .slogan__top {
    display: flex; align-items: center; gap: 14px;
  }
  .slogan__top::before, .slogan__top::after {
    content: ""; flex: 1; height: 1px; background: var(--rule);
  }
  .slogan__bottom {
    padding-bottom: 10px;
    border-bottom: 1px solid var(--rule);
  }

  /* back */
  .contact {
    position: absolute;
    left: 48px;
    color: var(--ink-dark);
  }
  .contact--first { top: 44px; }
  .contact--second { top: 268px; }
  .contact__name {
    font-weight: 700;
    font-size: 19px;
    text-transform: uppercase;
    letter-spacing: 0.3px;
  }
  .contact__phone {
    display: flex; align-items: center; gap: 6px;
    font-size: 17px;
    margin-top: 2px;
  }
  .icon { width: 16px; height: 16px; fill: var(--ink-dark); flex: none; }
  .card--back .brand-name {
    position: absolute;
    top: 170px; right: 56px;
    font-size: 44px;
    color: var(--ink-grey);
  }
  .links {
    position: absolute;
    right: 44px; bottom: 34px;
    text-align: right;
    color: var(--ink-dark);
    font-size: 18px;
    line-height: 1.4;
  }
  .links__row { display: flex; align-items: center; justify-content: flex-end; gap: 8px; }
</style>
</head>
<body>

<section class="card card--front">
  <div class="brand-name">Talbek vodka</div>
  <div class="slogan">
    <div class="slogan__top">What binds us</div>
    <div class="slogan__bottom">Organic and permium vodka</div>
  </div>
</section>

<section class="card card--back">
  <div class="contact contact--first">
    <div class="contact__name">Mateo Ignacio Dalmau Ferrerons</div>
    <div class="contact__phone">
      <svg class="icon" viewBox="0 0 24 24" aria-hidden="true"><path d="M6.6 10.8a15.1 15.1 0 0 0 6.6 6.6l2.2-2.2a1 1 0 0 1 1-.25 11.4 11.4 0 0 0 3.6.57 1 1 0 0 1 1 1V20a1 1 0 0 1-1 1A17 17 0 0 1 3 4a1 1 0 0 1 1-1h3.5a1 1 0 0 1 1 1c0 1.25.2 2.45.57 3.6a1 1 0 0 1-.25 1z"/></svg>
      +34 655 219 870
    </div>
  </div>

  <div class="brand-name">Talbek vodka</div>

  <div class="contact contact--second">
    <div class="contact__name">Oriol Batlle Quintana</div>
    <div class="contact__phone">
      <svg class="icon" viewBox="0 0 24 24" aria-hidden="true"><path d="M6.6 10.8a15.1 15.1 0 0 0 6.6 6.6l2.2-2.2a1 1 0 0 1 1-.25 11.4 11.4 0 0 0 3.6.57 1 1 0 0 1 1 1V20a1 1 0 0 1-1 1A17 17 0 0 1 3 4a1 1 0 0 1 1-1h3.5a1 1 0 0 1 1 1c0 1.25.2 2.45.57 3.6a1 1 0 0 1-.25 1z"/></svg>
      +34 677 341 592
    </div>
  </div>

  <div class="links">
    <div class="links__row">talbekvodka@mailora.net
      <svg class="icon" viewBox="0 0 24 24" aria-hidden="true"><path d="M2 5h20v14H2z M3.5 6.5 12 13l8.5-6.5" fill="none" stroke="#6f6f73" stroke-width="2"/></svg>
    </div>
    <div class="links__row">www.talbekvodkaorg.net
      <svg class="icon" viewBox="0 0 24 24" aria-hidden="true"><circle cx="12" cy="12" r="10"/><path d="M2 12h20M12 2c3 3 3 17 0 20M12 2c-3 3-3 17 0 20" fill="none" stroke="#fff" stroke-width="1.4"/></svg>
    </div>
  </div>
</section>

</body>
</html>
```